Patient Report Folder for modern Chiropractic Clinic

We are looking for someone to design a patient folder and 3 simple info sheets to go along with it.

The design should be clean and masculine with an artsy touch. I am a fan of the Del Morano style drawings so would like the background to be a style of parchment paper. The info sheets should follow a similar style.

Please check the “Design Outline” pdf and the “Folder Design” file before getting started. The 3 info sheets are going to be placed in the pocket where “Attachment #3” will be.

- The format should be DIN A4 according to the printing details attached in the files section. Please see the ''Folder Design.jpg'' for the design of the folder.
- All the designs should be different and unique in nature but match each other.
- The text for Info Sheet #3 can be left blank.

It is probably best to take a look at the ''Design Outline'' file first to see how I envision the design to be. Please do not hesitate to ask me questions or to discuss ideas.

Target Market(s)

upper class audience with a focus on health and well-being

Industry/Entity Type

Chiropractic // Health

Requirements
Must have
• The colours should be fitting with the main colours in the logo: #1ccad5 and #b1b2b4
Nice to have
• Del Morano Style design and the background on parchment paper style. It is not a must but if anyone can come up with a suitable design and colorway that would be great.

```html
<!DOCTYPE html>
<html lang="en">
<head>
<meta charset="utf-8">
<title>Spinewell Patient Folder</title>
<link rel="stylesheet" href="https://fonts.googleapis.com/css2?family=Michroma&family=Arimo:wght@400;700&display=swap">
<style>
  :root {
    --teal: #1ccad5;
    --teal-deep: #0f8f98;
    --grey: #b1b2b4;
    --ink: #2b2b2b;
    --night: #0c0c0c;
    --paper: #f3f3f3;
    --stage: #c9c9c9;
    --head: "Michroma", sans-serif;
    --body: "Arimo", sans-serif;
  }
  * { box-sizing: border-box; margin: 0; padding: 0; }
  html, body { width: 979px; height: 1200px; overflow: hidden; }
  body { background: var(--stage); font-family: var(--body); color: var(--ink); position: relative; }

  .spread { position: absolute; left: 89px; width: 800px; height: 566px; background: var(--paper); overflow: hidden; box-shadow: 0 4px 14px rgba(0,0,0,.18); }
  .spread--outside { top: 22px; }
  .spread--inside { top: 612px; }
  .spread__art { position: absolute; inset: 0; width: 800px; height: 566px; }
  .spread__fold { position: absolute; left: 399px; top: 0; width: 2px; height: 100%; background: linear-gradient(90deg, rgba(0,0,0,.12), rgba(255,255,255,.2)); }

  /* Outside cover */
  .brand { position: absolute; left: 70px; top: 130px; display: flex; align-items: center; gap: 16px; }
  .brand__dot { width: 86px; height: 86px; border: 3px solid var(--teal); border-radius: 50%; flex: none; }
  .brand__name { font-family: var(--head); font-size: 28px; color: var(--teal); letter-spacing: 1px; }

  .quote { position: absolute; left: 470px; top: 56px; width: 300px; font-family: var(--head); font-size: 18px; line-height: 1.35; color: #fff; text-align: center; letter-spacing: .5px; }

  .patient { position: absolute; left: 170px; top: 488px; width: 200px; }
  .patient__label { font-family: var(--head); font-size: 13px; color: var(--teal); margin-bottom: 10px; }
  .patient__line { border-bottom: 1px dashed var(--grey); height: 20px; }

  .contact { position: absolute; }
  .contact__phone { font-family: var(--head); font-size: 21px; color: var(--teal); letter-spacing: 1px; white-space: nowrap; }
  .contact__web { font-family: var(--head); font-size: 11px; margin-top: 6px; letter-spacing: 1px; white-space: nowrap; }
  .contact--cover { left: 470px; top: 468px; }
  .contact--cover .contact__web { color: #8c8d8f; }
  .contact--inside { left: 34px; top: 360px; }
  .contact--inside .contact__web { color: #fff; }

  /* Inside spread */
  .tab { position: absolute; display: flex; align-items: flex-end; }
  .tab__label { background: var(--teal); color: #fff; font-family: var(--head); font-size: 11px; padding: 4px 20px 3px 8px; clip-path: polygon(0 0, 88% 0, 100% 100%, 0 100%); white-space: nowrap; }
  .tab__rule { height: 3px; background: var(--teal); flex: 1; }
  .tab--visit { left: 30px; top: 30px; width: 350px; }
  .tab--stress { left: 425px; top: 96px; width: 350px; }

  .visit { position: absolute; left: 30px; top: 58px; width: 340px; list-style: none; }
  .visit__item { border-bottom: 1px solid #9a9a9a; padding: 4px 0 3px 12px; position: relative; font-size: 9.5px; line-height: 1.3; }
  .visit__item::before { content: ""; position: absolute; left: 0; top: 6px; border-left: 7px solid var(--teal); border-top: 4px solid transparent; border-bottom: 4px solid transparent; }
  .visit__title { color: var(--ink); }
  .visit__step { color: #444; }

  .stress__intro { position: absolute; left: 425px; top: 122px; width: 345px; font-size: 7.5px; line-height: 1.35; color: #555; }
  .stress__list { position: absolute; left: 425px; top: 160px; width: 180px; }
  .stress__item { margin-bottom: 12px; }
  .stress__name { font-family: var(--head); font-size: 9px; color: var(--teal); margin-bottom: 2px; }
  .stress__text { font-size: 9px; line-height: 1.3; color: #333; }
  .stress__photo { position: absolute; left: 620px; top: 160px; width: 150px; height: 175px; border: 2px solid var(--teal); border-radius: 12px; background: linear-gradient(160deg, #f7f7f5, #d9d3c8 60%, #b89a6f); }
</style>
</head>
<body>

<section class="spread spread--outside" aria-label="Folder outside">
  <svg class="spread__art" viewBox="0 0 800 566" role="img" aria-label="Clinic interior photo under a dark-to-teal tint">
    <defs>
      <linearGradient id="coverTint" x1="0" y1="0" x2="1" y2="0">
        <stop offset="0" stop-color="#262626"/>
        <stop offset=".42" stop-color="#2e3a3b"/>
        <stop offset=".55" stop-color="#137c84"/>
        <stop offset="1" stop-color="#2bb9c2"/>
      </linearGradient>
    </defs>
    <path d="M0,0 H800 V270 C740,370 600,420 470,430 C430,434 400,440 400,445 C250,420 90,440 30,566 H0 Z" fill="url(#coverTint)"/>
    <path d="M800,270 C740,370 600,420 470,430 C430,434 400,440 400,445 C250,420 90,440 30,566" fill="none" stroke="#b1b2b4" stroke-width="4"/>
    <path d="M800,286 C744,386 604,434 472,444 C432,448 404,454 402,458 C256,434 100,452 44,566" fill="none" stroke="#1ccad5" stroke-width="6"/>
  </svg>
  <div class="spread__fold"></div>

  <div class="brand">
    <span class="brand__dot"></span>
    <span class="brand__name">SPINEWELL</span>
  </div>

  <p class="quote">THE GREATEST<br>WEALTH IS HEALTH<br>-TALVEN-</p>

  <div class="patient">
    <p class="patient__label">PATIENT NAME</p>
    <div class="patient__line"></div>
    <div class="patient__line"></div>
  </div>

  <div class="contact contact--cover">
    <p class="contact__phone">0711 40512266</p>
    <p class="contact__web">www.spinewell-praxis.de</p>
  </div>
</section>

<section class="spread spread--inside" aria-label="Folder inside">
  <svg class="spread__art" viewBox="0 0 800 566" role="img" aria-label="Photo of a patient relaxing in the waiting area under a black-to-teal tint">
    <defs>
      <linearGradient id="insideTint" x1="0" y1="0" x2="1" y2="0.3">
        <stop offset="0" stop-color="#050505"/>
        <stop offset=".3" stop-color="#0d3e42"/>
        <stop offset=".55" stop-color="#1aa9b2"/>
        <stop offset="1" stop-color="#34dbe2"/>
      </linearGradient>
    </defs>
    <path d="M0,300 C120,268 300,300 420,420 C520,510 680,520 800,440 V566 H0 Z" fill="url(#insideTint)"/>
    <path d="M420,420 C520,510 680,520 800,440" fill="none" stroke="#b1b2b4" stroke-width="3" transform="translate(0,-6)"/>
  </svg>
  <div class="spread__fold"></div>

  <div class="tab tab--visit"><span class="tab__label">YOUR NEXT VISIT</span><span class="tab__rule"></span></div>
  <ul class="visit">
    <li class="visit__item"><p class="visit__title">Make yourself at home</p><p class="visit__step">Take off your shoes and jacket</p></li>
    <li class="visit__item"><p class="visit__title">Let us know you're here</p><p class="visit__step">Check in at the front desk</p></li>
    <li class="visit__item"><p class="visit__title">Get comfy</p><p class="visit__step">Take a seat in the waiting area or the designated adjusting room</p></li>
    <li class="visit__item"><p class="visit__title">Be excited and be ready</p><p class="visit__step">Take off your belt, empty your pockets and take a seat on "The Chair"</p></li>
    <li class="visit__item"><p class="visit__title">ADJUSTING TIME</p></li>
    <li class="visit__item"><p class="visit__title">Time to say goodbye</p><p class="visit__step">Our front desk will help you with EVERYTHING else you need</p></li>
    <li class="visit__item"><p class="visit__title">Be a better version of yourself</p><p class="visit__step">Take a 10 minute walk :)</p></li>
  </ul>

  <div class="contact contact--inside">
    <p class="contact__phone">0711 40512266</p>
    <p class="contact__web">www.spinewell-praxis.de</p>
  </div>

  <div class="tab tab--stress"><span class="tab__label">STRESS BUILDERS</span><span class="tab__rule"></span></div>
  <p class="stress__intro">Try your best to remove or reduce these stressors from your life where possible; fewer stressors let your body heal faster.</p>
  <div class="stress__list">
    <div class="stress__item"><p class="stress__name">EMOTIONAL</p><p class="stress__text">Your body being in a constant fight or flight state rather than a relaxed state.</p></div>
    <div class="stress__item"><p class="stress__name">CHEMICAL</p><p class="stress__text">Toxins in food, drink, pharmaceuticals, skin care and cleaning products all put stress on the body.</p></div>
    <div class="stress__item"><p class="stress__name">PHYSICAL</p><p class="stress__text">Any physical influence your body has had to compensate for, such as sports injuries or car accidents.</p></div>
  </div>
  <div class="stress__photo" role="img" aria-label="Photo of the chiropractic adjusting table"></div>
</section>

</body>
</html>
```